Set of ads for a Medical Clinic in Costa Blanca Spain

We will start a small medical clinic for general medicine for Swedish and Scandinavians living on Costa Blanca Spain.
The clinic is called LuvenClinic
We need a set of ads with different sizes and also looking for a Designer to work with longtime.

Sizes of the adds:
One add with size 95 mm x 128 mm
One add with size 192 x 128 mm

We want one version of the add with a sign across the add "Öppnar i November" meaning "Opening in November" That add will be like a teaser and just creating attention to the clinic.

Skandinavisk Vårdcentral Costa Blanca

- Hembesök/Mobil Vårdcentral
- Lättakut
- Uppföljning av blodtryck, diabetes

Läs mer och boka din tid enkelt på www.luvenclinic-demo.com
Hitta hit:
Kliniken ligger utmed N418 vid Playa Serenta, mitt emot Tolvarena
Av. Ramón Lusera 7-2, 03412 Villasort Baja

I have added pixelgrove images that could be used if you want, also open for other suggestions.

Target Market(s)

Swedish and Scandinavian patients looking for medical care in Spain

Industry/Entity Type

Medical

Colors
33b8a4
33a6d7
85cae6

Requirements
Must have
• Add in two sizes and versions.
• One add with size 95 mm x 128 mm
• One add with size 192 x 128 mm
• We want one add as a teaser before the clinic is opening. The add a bit faded and the text "Öppnar i November" across the add on the side. And one version of the add without "Öppnar i November"

```html
<!DOCTYPE html>
<html lang="sv">
<head>
<meta charset="utf-8">
<title>LuvenClinic – annonser</title>
<link href="https://fonts.googleapis.com/css2?family=Open+Sans:wght@400;600&family=Ubuntu:wght@500&family=Oswald:wght@600&family=Archivo+Black&display=swap" rel="stylesheet">
<style>
  :root{
    --teal:#1fb0a0;
    --teal-dark:#16968a;
    --blue:#33a6d7;
    --ink:#2b2b2b;
    --grey:#6d7478;
    --ring:#c9cfd1;
    --photo-a:#e9dcd3;
    --photo-b:#c9b2a4;
    --bg:#f3efe9;
  }
  *{box-sizing:border-box;margin:0;padding:0}
  html,body{width:1200px;height:1003px;overflow:hidden;background:var(--bg)}
  body{position:relative;font-family:"Open Sans",sans-serif;color:var(--ink)}

  .ad{position:absolute;background:#fff;overflow:hidden;box-shadow:0 4px 10px rgba(0,0,0,.25)}
  .ad svg.shapes{position:absolute;left:0;top:0}
  .photo-fill{position:absolute}

  .brand{position:absolute;font-family:"Ubuntu",sans-serif;font-weight:500;color:var(--teal);line-height:1;white-space:nowrap}
  .tagline{position:absolute;color:var(--blue);line-height:1;white-space:nowrap}

  .services-title{position:absolute;background:var(--teal);color:#fff;text-align:center;border-radius:3px;line-height:1;display:flex;align-items:center;justify-content:center}
  .services{position:absolute;list-style:none}
  .services li{display:flex;align-items:center;gap:9px;white-space:nowrap}
  .services svg{flex:none}

  .caption{position:absolute;font-family:"Archivo Black",sans-serif;font-size:32px;color:#111;letter-spacing:.5px;white-space:nowrap}

  /* large flyer */
  .flyer{left:87px;top:112px;width:479px;height:718px}
  .flyer .brand{left:30px;top:400px;font-size:47px}
  .flyer .tagline{left:31px;top:444px;font-size:16px}
  .flyer .services-title{left:31px;top:486px;width:175px;height:25px;font-size:19px}
  .flyer .services{left:31px;top:522px;font-size:11.5px;line-height:19px}
  .opening-badge{position:absolute;left:249px;top:482px;width:184px;height:184px;border-radius:50%;border:7px solid var(--ring);background:radial-gradient(circle at 50% 30%,#6fd6c7 0%,var(--teal) 45%,var(--teal-dark) 100%);color:#fff;font-family:"Oswald",sans-serif;font-weight:600;text-align:center;display:flex;flex-direction:column;justify-content:center;line-height:1}
  .opening-badge .big{font-size:40px}
  .opening-badge .small{font-size:24px;margin-top:6px}
  .flyer .footer-address{position:absolute;left:24px;top:667px;font-size:10.5px;color:#fff;line-height:15px;display:flex;gap:6px;white-space:nowrap}
  .flyer .footer-web{position:absolute;right:22px;top:679px;font-size:10.5px;color:#fff;display:flex;gap:6px;align-items:center;white-space:nowrap}

  /* small ad */
  .card{left:634px;top:292px;width:480px;height:356px}
  .card .brand{left:264px;top:22px;font-size:33px}
  .card .tagline{left:265px;top:55px;font-size:12.5px}
  .card .services-title{left:264px;top:85px;width:175px;height:25px;font-size:18px}
  .card .services{left:264px;top:121px;font-size:10.5px;line-height:19.3px}
  .opening-banner{position:absolute;left:255px;top:206px;width:212px;height:36px;display:flex;align-items:center;justify-content:center;color:#fff;font-family:"Oswald",sans-serif;font-weight:600;font-size:21px;white-space:nowrap}
  .card .address{position:absolute;left:264px;top:254px;font-size:10.5px;line-height:14.5px;display:flex;gap:7px;white-space:nowrap}
  .card .web{position:absolute;left:264px;top:326px;font-size:10.5px;display:flex;gap:7px;align-items:center;white-space:nowrap}
</style>
</head>
<body>

<!-- 192 x 128 mm -->
<section class="ad flyer">
  <div class="photo-fill" role="img" aria-label="Foto: läkare undersöker en leende flicka medan mamman håller om henne" style="left:0;top:0;width:479px;height:370px;background:linear-gradient(135deg,var(--photo-a),var(--photo-b))"></div>
  <svg class="shapes" width="479" height="718" viewBox="0 0 479 718" aria-hidden="true">
    <path d="M0 250 Q120 340 300 320 Q420 305 479 260 L479 718 L0 718 Z" fill="var(--teal)"/>
    <path d="M0 262 Q130 360 300 335 Q420 318 479 285 L479 718 L0 718 Z" fill="#fff"/>
    <path d="M0 610 Q200 640 479 570 L479 718 L0 718 Z" fill="var(--grey)"/>
    <path d="M0 618 Q200 655 479 585 L479 718 L0 718 Z" fill="var(--teal)"/>
    <circle cx="96" cy="315" r="76" fill="var(--teal)"/>
  </svg>
  <div class="photo-fill" role="img" aria-label="Foto: läkare med stetoskop undersöker ett barn med nalle" style="left:26px;top:245px;width:140px;height:140px;border-radius:50%;background:linear-gradient(135deg,#f1ece8,#d9c6bb)"></div>

  <div class="brand">LuvenClinic</div>
  <div class="tagline">Skandinavisk Läkarmottagning</div>

  <div class="services-title">VÅRA TJÄNSTER</div>
  <ul class="services">
    <li><svg width="14" height="12" viewBox="0 0 14 12"><path d="M1 6 L5 10 L13 1" fill="none" stroke="var(--teal)" stroke-width="2"/></svg>Diabetes</li>
    <li><svg width="14" height="12" viewBox="0 0 14 12"><path d="M1 6 L5 10 L13 1" fill="none" stroke="var(--teal)" stroke-width="2"/></svg>Lättakut</li>
    <li><svg width="14" height="12" viewBox="0 0 14 12"><path d="M1 6 L5 10 L13 1" fill="none" stroke="var(--teal)" stroke-width="2"/></svg>Uppföljning av blodtryck</li>
    <li><svg width="14" height="12" viewBox="0 0 14 12"><path d="M1 6 L5 10 L13 1" fill="none" stroke="var(--teal)" stroke-width="2"/></svg>Hembesök/Mobil Vårdcentral</li>
  </ul>

  <div class="opening-badge"><span class="big">Öppnar</span><span class="small">I November</span></div>

  <div class="footer-address">
    <svg width="12" height="14" viewBox="0 0 12 14"><path d="M6 13 C2 8 1 6.5 1 5 A5 5 0 0 1 11 5 C11 6.5 10 8 6 13 Z" fill="#fff"/><circle cx="6" cy="5" r="2" fill="var(--teal)"/></svg>
    <p>Kliniken ligger utmed N418 vid Playa Serenta,<br>mitt emot Tolvarena Av. Ramón Lusera 7-2,<br>03412 Villasort Baja</p>
  </div>
  <div class="footer-web">
    <svg width="13" height="13" viewBox="0 0 13 13"><circle cx="6.5" cy="6.5" r="5.5" fill="none" stroke="#fff"/><ellipse cx="6.5" cy="6.5" rx="2.5" ry="5.5" fill="none" stroke="#fff"/><path d="M1 6.5 H12" stroke="#fff"/></svg>
    www.luvenclinic-demo.com
  </div>
</section>
<div class="caption" style="left:182px;top:862px">192MM X 128MM</div>

<!-- 95 x 128 mm -->
<section class="ad card">
  <div class="photo-fill" role="img" aria-label="Foto: mamma och dotter hos läkaren, flickan ler" style="left:0;top:0;width:250px;height:356px;background:linear-gradient(135deg,var(--photo-a),var(--photo-b))"></div>
  <svg class="shapes" width="480" height="356" viewBox="0 0 480 356" aria-hidden="true">
    <path d="M190 0 Q260 90 255 190 Q250 290 210 356 L480 356 L480 0 Z" fill="var(--teal)"/>
    <path d="M208 0 Q278 95 272 190 Q266 290 228 356 L480 356 L480 0 Z" fill="#fff"/>
    <circle cx="187" cy="278" r="66" fill="var(--teal)"/>
    <polygon points="255,206 467,206 459,224 467,242 255,242 263,224" fill="var(--teal)"/>
    <polygon points="263,242 460,242 456,248 267,248" fill="var(--grey)"/>
  </svg>
  <div class="photo-fill" role="img" aria-label="Foto: läkare med stetoskop undersöker ett barn med nalle" style="left:129px;top:220px;width:116px;height:116px;border-radius:50%;background:linear-gradient(135deg,#f1ece8,#d9c6bb)"></div>

  <div class="brand">LuvenClinic</div>
  <div class="tagline">Skandinavisk Läkarmottagning</div>

  <div class="services-title">VÅRA TJÄNSTER</div>
  <ul class="services">
    <li><svg width="14" height="12" viewBox="0 0 14 12"><path d="M1 6 L5 10 L13 1" fill="none" stroke="var(--teal)" stroke-width="2"/></svg>Diabetes</li>
    <li><svg width="14" height="12" viewBox="0 0 14 12"><path d="M1 6 L5 10 L13 1" fill="none" stroke="var(--teal)" stroke-width="2"/></svg>Lättakut</li>
    <li><svg width="14" height="12" viewBox="0 0 14 12"><path d="M1 6 L5 10 L13 1" fill="none" stroke="var(--teal)" stroke-width="2"/></svg>Uppföljning av blodtryck</li>
    <li><svg width="14" height="12" viewBox="0 0 14 12"><path d="M1 6 L5 10 L13 1" fill="none" stroke="var(--teal)" stroke-width="2"/></svg>Hembesök/Mobil Vårdcentral</li>
  </ul>

  <div class="opening-banner">Öppnar I November</div>

  <div class="address">
    <svg width="12" height="14" viewBox="0 0 12 14"><path d="M6 13 C2 8 1 6.5 1 5 A5 5 0 0 1 11 5 C11 6.5 10 8 6 13 Z" fill="var(--teal)"/><circle cx="6" cy="5" r="2" fill="#fff"/></svg>
    <p>Kliniken ligger utmed<br>N418 vid Playa Serenta,<br>mitt emot Tolvarena<br>Av. Ramón Lusera 7-2,<br>03412 Villasort Baja</p>
  </div>
  <div class="web">
    <svg width="13" height="13" viewBox="0 0 13 13"><circle cx="6.5" cy="6.5" r="5.5" fill="none" stroke="var(--teal)"/><ellipse cx="6.5" cy="6.5" rx="2.5" ry="5.5" fill="none" stroke="var(--teal)"/><path d="M1 6.5 H12" stroke="var(--teal)"/></svg>
    www.luvenclinic-demo.com
  </div>
</section>
<div class="caption" style="left:739px;top:674px">95MM X 128MM</div>

</body>
</html>
```